Ecommerce site for Bramwell Dovey Company

This is an ecommerce store design and will be based on the xcart ecommerce platform, attached is a design specification and all images to use in the design, you may use any other images you see fit.
This is a new Company so has no logo, if possible please create a logo but if not just use a text based logo in the design this maybe replaced later if required.
We only require a Home page design initially but will also need a category and product page design created, if you can do those also it would be an advantage.
IMPORTANT
We require all designs to be supplied as a full size JPG so we can see the design in detail as the pixel quarry previews are often too small.

```html
<!DOCTYPE html>
<html lang="en">
<head>
<meta charset="utf-8">
<title>Bramwell Dovey — Home</title>
<link rel="stylesheet" href="https://fonts.googleapis.com/css2?family=Arimo:wght@400;700&family=Open+Sans:wght@400&display=swap">
<style>
:root{
  --backdrop:#dcdcdc;
  --page:#f4f4f4;
  --band:#1b1b1b;
  --ink:#111111;
  --ink-soft:#333333;
  --muted:#7a7a7a;
  --rule:#d0d0d0;
  --white:#ffffff;
  --slide:#b9b9b9;
  --dot:#222222;
  --promo:#ff0000;
  --flag-blue:#1f3c8a;
  --flag-red:#d0162a;
}
*{margin:0;padding:0;box-sizing:border-box}
html,body{width:1200px;height:975px;overflow:hidden;background:var(--backdrop)}
body{position:relative;font-family:"Arimo",Arial,sans-serif;color:var(--ink)}
.page{position:absolute;left:25px;top:0;width:1150px;height:975px;background:var(--page)}
.abs{position:absolute}

/* header */
.brand{left:63px;top:80px;font-size:33px;font-weight:700;color:var(--ink);white-space:nowrap}
.cart-summary{right:13px;top:22px;display:flex;align-items:center;gap:8px;font-size:18px;color:var(--ink-soft)}
.cart-summary b{font-weight:700}
.account-nav{right:18px;top:72px;display:flex;align-items:center;font-size:14px;color:var(--muted)}
.account-nav a{display:flex;align-items:center;gap:6px;color:inherit;text-decoration:none;padding:0 8px;border-left:1px solid var(--rule)}
.account-nav a:first-child{border-left:none;color:var(--ink-soft)}
.prefs{right:17px;top:106px;display:flex;align-items:center;gap:10px;font-size:14px;color:var(--muted)}
.select{width:126px;height:28px;border:1px solid var(--rule);background:var(--white);display:flex;align-items:center;justify-content:space-between;padding-left:10px;font-size:13px;color:#aaa}
.select span.caret{width:28px;height:100%;border-left:1px solid var(--rule);display:flex;align-items:center;justify-content:center}
.search{right:17px;top:143px;display:flex;align-items:center;gap:6px}
.search .field{width:279px;height:28px;border:1px solid var(--rule);background:var(--white);font-size:12px;color:#444;display:flex;align-items:center;justify-content:space-between;padding:0 8px}
.search .label{font-size:18px;font-weight:700;color:var(--ink-soft)}

/* band */
.band{left:0;top:185px;width:1150px;height:663px;background:var(--band)}
.slide{left:26px;top:21px;width:760px;height:314px;background:var(--slide)}
.dots{left:614px;top:286px;display:flex;gap:6px}
.dots i{width:19px;height:19px;border-radius:50%;background:var(--dot)}
.dots i.on{background:var(--white)}
.promo{left:892px;top:30px;width:150px;height:150px;border-radius:50%;background:var(--promo);display:flex;align-items:center;justify-content:center}
.promo p{transform:rotate(-27deg);text-align:center;color:var(--white);font-weight:700;font-size:16px;line-height:20px}
.categories{left:0;top:361px;width:353px}
.section-title{font-size:27px;font-weight:700;color:var(--white)}
.categories .section-title{padding-left:91px}
.dash-under{border-bottom:2px dashed var(--white);height:0}
.cat-list{list-style:none;margin-top:30px;padding-left:31px;width:318px}
.cat-list li{font-size:24px;color:var(--white);height:46px;display:flex;align-items:center;gap:20px;border-bottom:1px dashed var(--white)}
.cat-list li:last-child{border-bottom:none}
.cat-list li.current{font-weight:700}
.divider{left:352px;top:352px;height:300px;border-left:2px dashed var(--white)}
.about{left:407px;top:365px;width:646px}
.about p{font-family:"Open Sans",Arial,sans-serif;font-size:22px;line-height:30px;color:var(--white);margin-top:36px}
.about p + p{margin-top:30px}

/* footer */
.legal{left:0;top:869px;width:1150px;text-align:center;font-size:18px;font-weight:700;color:var(--ink-soft)}
.legal .sep{margin:0 22px}
.copyright{left:0;top:922px;width:1150px;text-align:center;padding-right:50px;font-size:18px;font-weight:700;color:var(--ink-soft)}
.payments{left:889px;top:893px;display:flex;gap:7px}
.payments span{width:74px;height:47px;border:1px solid #999;background:var(--white);display:flex;align-items:center;justify-content:center;font-size:13px;font-weight:700;color:#555}
</style>
</head>
<body>
<div class="page">
  <div class="abs brand">Bramwell Dovey</div>

  <div class="abs cart-summary">
    <svg width="40" height="36" viewBox="0 0 40 36" aria-hidden="true"><path d="M2 4h6l5 20h20l4-14H11" fill="none" stroke="#222" stroke-width="2.5"/><circle cx="15" cy="30" r="3" fill="#222"/><circle cx="31" cy="30" r="3" fill="#222"/></svg>
    <span>Now in your cart <b>0 Items</b></span>
  </div>

  <nav class="abs account-nav">
    <a href="#"><svg width="14" height="16" viewBox="0 0 14 16"><circle cx="7" cy="4" r="4" fill="#222"/><path d="M0 16c0-6 14-6 14 0z" fill="#222"/></svg>My Account</a>
    <a href="#"><svg width="16" height="16" viewBox="0 0 16 16"><path d="M8 0l2.4 5.2 5.6.6-4.2 3.8 1.2 5.6L8 12.4 3 15.2l1.2-5.6L0 5.8l5.6-.6z" fill="#777"/></svg>My Wishlist</a>
    <a href="#"><svg width="18" height="16" viewBox="0 0 18 16"><path d="M1 2h3l2 9h9l2-7H5" fill="none" stroke="#777" stroke-width="1.5"/><circle cx="7" cy="14" r="1.5" fill="#777"/><circle cx="14" cy="14" r="1.5" fill="#777"/></svg>My Cart</a>
    <a href="#"><svg width="18" height="16" viewBox="0 0 18 16"><path d="M1 2h3l2 9h9l2-7H5" fill="none" stroke="#777" stroke-width="1.5"/><circle cx="7" cy="14" r="1.5" fill="#777"/><circle cx="14" cy="14" r="1.5" fill="#777"/></svg>Checkout</a>
    <a href="#"><svg width="14" height="16" viewBox="0 0 14 16"><path d="M3 7V4a4 4 0 0 1 8 0v3" fill="none" stroke="#777" stroke-width="2"/><rect x="1" y="7" width="12" height="9" fill="#777"/></svg>Log In</a>
  </nav>

  <div class="abs prefs">
    <span>languages:</span>
    <svg width="34" height="20" viewBox="0 0 60 30" aria-label="English">
      <clipPath id="flag-clip"><rect width="60" height="30"/></clipPath>
      <g clip-path="url(#flag-clip)">
        <rect width="60" height="30" fill="var(--flag-blue)"/>
        <path d="M0 0L60 30M60 0L0 30" stroke="#fff" stroke-width="6"/>
        <path d="M0 0L60 30M60 0L0 30" stroke="var(--flag-red)" stroke-width="2"/>
        <path d="M30 0V30M0 15H60" stroke="#fff" stroke-width="10"/>
        <path d="M30 0V30M0 15H60" stroke="var(--flag-red)" stroke-width="6"/>
      </g>
    </svg>
    <span>currencies:</span>
    <div class="select">US Dollar<span class="caret"><svg width="14" height="8" viewBox="0 0 14 8"><path d="M1 1l6 6 6-6" fill="none" stroke="#888" stroke-width="1.5"/></svg></span></div>
  </div>

  <div class="abs search">
    <div class="field">Enter keywords here<span>&raquo;</span></div>
    <span class="label">Search</span>
  </div>

  <section class="abs band">
    <div class="abs slide" role="img" aria-label="Featured curtain track slideshow image"></div>
    <div class="abs dots"><i class="on"></i><i></i><i></i><i></i></div>

    <div class="abs promo"><p>Free UK delivery<br>on orders<br>over £100</p></div>

    <div class="abs categories">
      <h2 class="section-title">Categories</h2>
      <div class="dash-under" style="margin:6px 0 0 68px;width:218px"></div>
      <ul class="cat-list">
        <li class="current"><span>+</span>Quiet Glide Tracks</li>
        <li><span>+</span>Hand operated Tracks</li>
        <li><span>+</span>Cord operated Tracks</li>
        <li><span>+</span>Automated Tracks</li>
      </ul>
    </div>

    <div class="abs divider"></div>

    <div class="abs about">
      <h2 class="section-title">About Us</h2>
      <div class="dash-under" style="margin-top:4px"></div>
      <p>Our Company sells curtain tracks that your curtains hang on! We're a new business and are starting out with a limited number of products.</p>
      <p>Our target market is really any homeowner that wants to enhance their living environment with new curtain tracks. Women tend to be the main customer type initially.</p>
    </div>
  </section>

  <div class="abs legal">Terms &amp; Conditions<span class="sep">|</span>Privacy Policy</div>
  <div class="abs copyright">Copyright 2011-2012</div>
  <div class="abs payments">
    <span>Paysa</span><span>Meridian</span><span>Voyager</span>
  </div>
</div>
</body>
</html>
```